Stationery & Business Card Design For A Mobile Ultrasound Company
Ridgecrest Sonar Partners, Inc.
Professional
Martin L. Povich
Clinical Director
3187 Hawthorn Lane NE
Carrollton, OH 44892
ridgecrestsonarpartners@mailnest.example
www.ridgecrestsonarpartners.example

```html
<!DOCTYPE html>
<html lang="en">
<head>
<meta charset="utf-8">
<title>Ridgecrest Sonar Partners — Business Card</title>
<link href="https://fonts.googleapis.com/css2?family=Arimo:wght@400;700&display=swap" rel="stylesheet">
<style>
  :root {
    --page-bg: #e9e6e2;
    --card-white: #ffffff;
    --brand-blue: #2f7fbd;
    --brand-blue-dark: #1f5f95;
    --accent-red: #d23a3f;
    --ink-grey: #4a4a4a;
    --soft-grey: #6b6b6b;
  }
  * { margin: 0; padding: 0; box-sizing: border-box; }
  html, body {
    width: 1200px; height: 818px; overflow: hidden;
    background: var(--page-bg);
    font-family: "Arimo", Arial, sans-serif;
  }
  .card {
    position: absolute; left: 100px; top: 123px;
    width: 1000px; height: 572px;
    background: var(--card-white);
    border-radius: 26px;
    overflow: hidden;
    box-shadow: 0 6px 18px rgba(0,0,0,0.12);
  }
  .brand {
    position: absolute; left: 0; right: 0; top: 120px;
    display: flex; justify-content: center; align-items: center; gap: 18px;
  }
  .brand-mark {
    width: 46px; height: 46px; border-radius: 50%;
    background: var(--accent-red);
  }
  .brand-name {
    font-size: 54px; font-weight: 700; letter-spacing: 1px;
    color: var(--brand-blue);
    text-transform: uppercase;
  }
  .rule {
    position: absolute; left: 0; right: 0; height: 4px;
    background: var(--accent-red);
  }
  .rule-top { top: 262px; }
  .rule-bottom { top: 424px; }
  .contact-band {
    position: absolute; left: 0; right: 0; top: 274px; height: 140px;
    background: var(--brand-blue);
    color: #fff;
  }
  .address {
    position: absolute; right: 560px; top: 44px;
    text-align: right; font-size: 26px; line-height: 32px;
  }
  .divider {
    position: absolute; left: 462px; top: 10px; width: 2px; height: 120px;
    background: rgba(255,255,255,0.85);
  }
  .contact-list {
    position: absolute; left: 480px; top: 8px;
    list-style: none; font-size: 23px; line-height: 31px;
  }
  .contact-list li { display: flex; align-items: center; gap: 10px; }
  .contact-list svg { width: 20px; height: 20px; flex: none; }
  .signature {
    position: absolute; left: 0; right: 0; top: 470px;
    text-align: center; font-size: 28px; color: var(--soft-grey);
  }
  .signature .person { font-weight: 700; color: var(--ink-grey); }
</style>
</head>
<body>
  <div class="card">
    <div class="brand">
      <span class="brand-mark"></span>
      <span class="brand-name">Ridgecrest Sonar Partners</span>
    </div>

    <div class="rule rule-top"></div>
    <section class="contact-band">
      <p class="address">3187 Hawthorn Lane NE<br>Carrollton, OH 44892</p>
      <div class="divider"></div>
      <ul class="contact-list">
        <li>
          <svg viewBox="0 0 24 24"><path fill="#fff" d="M6.6 10.8a15 15 0 0 0 6.6 6.6l2.2-2.2a1 1 0 0 1 1-.25 11.4 11.4 0 0 0 3.6.57 1 1 0 0 1 1 1V20a1 1 0 0 1-1 1A17 17 0 0 1 3 4a1 1 0 0 1 1-1h3.5a1 1 0 0 1 1 1c0 1.25.2 2.45.57 3.6a1 1 0 0 1-.25 1z"/></svg>
          330-555-0148
        </li>
        <li>
          <svg viewBox="0 0 24 24"><rect x="6" y="2" width="12" height="20" rx="2" fill="#fff"/><rect x="8" y="5" width="8" height="12" fill="#2f7fbd"/></svg>
          330-555-0193
        </li>
        <li>
          <svg viewBox="0 0 24 24"><rect x="2" y="5" width="20" height="14" rx="2" fill="#fff"/><path d="M3 6l9 7 9-7" fill="none" stroke="#2f7fbd" stroke-width="2"/></svg>
          ridgecrestsonarpartners@mailnest.example
        </li>
        <li>
          <svg viewBox="0 0 24 24"><circle cx="12" cy="12" r="10" fill="#fff"/><path d="M2 12h20M12 2c3 3 3 17 0 20M12 2c-3 3-3 17 0 20" fill="none" stroke="#2f7fbd" stroke-width="1.6"/></svg>
          www.ridgecrestsonarpartners.example
        </li>
      </ul>
    </section>
    <div class="rule rule-bottom"></div>

    <p class="signature"><span class="person">Martin L. Povich,</span> Clinical Director</p>
  </div>
</body>
</html>
```